Tea bag packaging design for KELVIRA

Hello. I am creating a green tea and soybean tea, and I am looking for packaging designs. I will attach some designs I like and our current KELVIRA logo. Feel free to follow the designs or create something of your own.

Package size is 200 (W) x 290(L) mm

The package is a white aluminum package so it can accommodate a wide range of colors. We don't want to pay a ton in printing so 5 colors or less is nice. But we will make exceptions for something more colorful if it's well done.

Target Market(s)

Women and Men in 30s-40s

Industry/Entity Type

food and beverage

Font styles to use
Sans Serif
Other font styles liked:
• red hat is the font of the logo

Requirements
Must have
• clean, simple, but bold design
Nice to have
• images of soybeans and green tea leaves on the package

```html
<!DOCTYPE html>
<html lang="en">
<head>
<meta charset="utf-8">
<title>KELVIRA Tea – Pouch Front</title>
<link rel="stylesheet" href="https://fonts.googleapis.com/css2?family=Red+Hat+Display:wght@600;700;800;900&display=swap">
<style>
  :root {
    --canvas-bg: #d6d6d6;
    --leaf-green: #62a034;
    --glow-green: #a6d04c;
    --deep-green: #3f6e22;
    --cream: #eef3bb;
    --cream-soft: #f2f5c8;
    --white: #ffffff;
    --ink: #1f2a14;
    --cup-tone: #ddd9c6;
  }
  * { margin: 0; padding: 0; box-sizing: border-box; }
  html, body {
    width: 1200px; height: 1117px; overflow: hidden;
    background: var(--canvas-bg);
    font-family: "Red Hat Display", sans-serif;
  }
  .pack-front {
    position: absolute; left: 255px; top: 58px;
    width: 690px; height: 1000px; overflow: hidden;
    background: radial-gradient(ellipse 65% 45% at 50% 30%, var(--glow-green) 0%, var(--leaf-green) 78%);
  }
  .pack-art { position: absolute; inset: 0; }
  .leaf-sprig {
    position: absolute; border-radius: 50%;
    background: radial-gradient(ellipse at 50% 50%, rgba(183,220,106,0.75) 0%, rgba(140,196,74,0.35) 55%, rgba(106,164,58,0) 72%);
  }
  .leaf-sprig--left { left: -20px; top: 168px; width: 150px; height: 150px; }
  .leaf-sprig--right { left: 520px; top: 102px; width: 180px; height: 230px; }
  .brand-badge {
    position: absolute; left: 247px; top: 135px; width: 194px; height: 194px;
    border-radius: 50%; background: var(--cream);
    display: flex; align-items: center; justify-content: center;
  }
  .brand-badge__name {
    font-weight: 800; font-size: 26px; color: var(--ink); letter-spacing: 0.5px;
  }
  .product-line {
    position: absolute; left: 0; top: 432px; width: 690px; text-align: center;
    color: var(--white); font-weight: 800; font-size: 28px; line-height: 1;
  }
  .organic-claim {
    position: absolute; left: 520px; top: 536px; width: 130px; color: var(--cream);
    text-align: center; line-height: 1;
  }
  .organic-claim__pct { display: block; font-weight: 700; font-size: 34px; }
  .organic-claim__pure { display: block; font-weight: 900; font-size: 40px; }
  .organic-claim__word { display: block; font-weight: 800; font-size: 21px; margin-top: 1px; }
  .serving-photo {
    position: absolute; left: 150px; top: 655px; width: 406px; height: 258px;
    border-radius: 28px; background: var(--cup-tone);
  }
  .diet-mark {
    position: absolute; top: 849px; width: 110px; text-align: center;
    font-weight: 800; font-size: 12px; color: var(--deep-green);
  }
  .diet-mark svg { display: block; margin: 0 auto 6px; }
  .diet-mark--gmo { left: 40px; }
  .diet-mark--gluten { left: 538px; }
  .net-weight {
    position: absolute; left: 0; top: 952px; width: 690px; text-align: center;
    font-weight: 800; font-size: 16px; letter-spacing: 2px; color: var(--deep-green); line-height: 1;
  }
</style>
</head>
<body>
  <main class="pack-front">
    <svg class="pack-art" width="690" height="1000" viewBox="0 0 690 1000" aria-hidden="true">
      <path class="base-band" d="M0 822 Q345 744 690 822 L690 1000 L0 1000 Z" fill="var(--cream-soft)"/>
      <circle cx="178" cy="296" r="4" fill="#d9f08a" opacity="0.8"/>
      <circle cx="95" cy="508" r="6" fill="#d9f08a" opacity="0.8"/>
      <circle cx="495" cy="257" r="4" fill="#d9f08a" opacity="0.8"/>
      <circle cx="627" cy="499" r="3" fill="#d9f08a" opacity="0.8"/>
      <circle cx="533" cy="143" r="3" fill="#d9f08a" opacity="0.8"/>
      <path id="title-arc" d="M60 442 Q345 368 630 442" fill="none"/>
      <text font-family="Red Hat Display, sans-serif" font-weight="900" font-size="66" fill="var(--cream)" text-anchor="middle" letter-spacing="3">
        <textPath href="#title-arc" startOffset="50%">KELVIRA TEA</textPath>
      </text>
    </svg>

    <div class="leaf-sprig leaf-sprig--left" role="img" aria-label="Fresh green tea leaves"></div>
    <div class="leaf-sprig leaf-sprig--right" role="img" aria-label="Sprig of green tea leaves"></div>

    <div class="brand-badge"><span class="brand-badge__name">KELVIRA</span></div>

    <p class="product-line">TEA LEAF AND SOYBEAN</p>

    <p class="organic-claim">
      <span class="organic-claim__pct">100%</span>
      <span class="organic-claim__pure">PURE</span>
      <span class="organic-claim__word">ORGANIC</span>
    </p>

    <div class="serving-photo" role="img" aria-label="Glass cup of tea on a saucer with tea leaves and a wooden spoon of soybeans"></div>

    <div class="diet-mark diet-mark--gmo">
      <svg width="54" height="54" viewBox="0 0 54 54" aria-hidden="true">
        <circle cx="27" cy="27" r="24" fill="none" stroke="var(--deep-green)" stroke-width="2.5"/>
        <line x1="10" y1="44" x2="44" y2="10" stroke="var(--deep-green)" stroke-width="2.5"/>
      </svg>
      NON GMO
    </div>
    <div class="diet-mark diet-mark--gluten">
      <svg width="54" height="54" viewBox="0 0 54 54" aria-hidden="true">
        <circle cx="27" cy="27" r="24" fill="none" stroke="var(--deep-green)" stroke-width="2.5"/>
        <line x1="27" y1="14" x2="27" y2="42" stroke="var(--deep-green)" stroke-width="2.5"/>
        <path d="M27 24 Q20 22 19 16 M27 24 Q34 22 35 16 M27 32 Q20 30 19 24 M27 32 Q34 30 35 24" fill="none" stroke="var(--deep-green)" stroke-width="2.5"/>
        <line x1="10" y1="44" x2="44" y2="10" stroke="var(--deep-green)" stroke-width="2.5"/>
      </svg>
      GLUTEN FREE
    </div>

    <p class="net-weight">NET 10 OZ (283 G)</p>
  </main>
</body>
</html>
```